Redesign of an existing webpage

We've just redesigned our logo on a new website design to reflect the new logo. That wants to change the color and graphical appearance of our website. There are no restrictions on what should be changed. IT should display our portfolio and pricing and explain our product. Please provide stock photos if needed. The site structure should not be changed. So we want the pages which are currently there. We need the following pages: Main page (Home page) Detail page (currently used at AGB and questions) Imprint (including the map) existing webpage: www.brightdune.de
Updates

I've got a request from one of the designers-

Target Market(s)

We are offering IT services to small companies. The do not need own IT equipment or PC Specialists if if our service.

Industry/Entity Type

It Service

Coding

Coded - Design and coding required

Number of Pages Required

3 page

Font styles to use
Other font styles liked:
• Relaway

Colors

Designer to choose colors to be used in the design.

Requirements
Must have
• our login mask at https://desktop.brightdune.com needs a rebranding too

```html
<!DOCTYPE html>
<html lang="en">
<head>
<meta charset="utf-8">
<title>BrightDune – IT that just works</title>
<link rel="stylesheet" href="https://fonts.googleapis.com/css2?family=Raleway:wght@400;500;600;700;800&family=Open+Sans:wght@400;600&display=swap">
<style>
:root{
  --blue:#1a5aa8;
  --blue-strong:#0e57b3;
  --navy:#0f1a33;
  --hero:#1b2433;
  --band:#ebf0f9;
  --ink:#2c2f36;
  --muted:#5d6270;
  --white:#ffffff;
  --dot:#9a9ca3;
}
*{box-sizing:border-box;margin:0;padding:0}
html,body{width:1200px;height:4082px;overflow:hidden}
body{position:relative;background:var(--white);font-family:"Open Sans",Arial,sans-serif;color:var(--ink)}
.abs{position:absolute}
.backdrop{position:absolute;left:0;top:0;width:1200px;height:4082px}
.raleway{font-family:"Raleway",Arial,sans-serif}

/* header */
.brand{left:144px;top:28px;font-family:"Raleway",sans-serif;font-weight:800;font-size:27px;letter-spacing:2px;color:var(--white);display:flex;align-items:center;gap:10px}
.brand-dot{width:14px;height:14px;border-radius:50%;background:var(--blue-strong);display:inline-block}
.nav{right:146px;top:34px;display:flex;gap:30px;font-family:"Raleway",sans-serif;font-size:12.5px;color:var(--white);text-transform:uppercase}
.nav .active{color:#3d8ae6}

.hero-photo{left:0;top:0;width:1200px;height:693px}
.hero-title{left:0;width:1200px;top:254px;text-align:center;font-family:"Raleway",sans-serif;font-size:40px;color:var(--white)}
.hero-text{left:150px;width:900px;top:308px;text-align:center;font-family:"Raleway",sans-serif;font-size:13px;line-height:24px;color:#e6e9ef}
.btn-blue{left:517px;top:371px;width:168px;height:38px;background:var(--blue-strong);color:var(--white);font-family:"Raleway",sans-serif;font-weight:600;font-size:12.5px;display:flex;align-items:center;justify-content:center}
.arrow{top:322px}

/* section titles */
.section-title{left:0;width:1200px;text-align:center;font-family:"Raleway",sans-serif;font-size:40px;color:var(--blue)}

.feature{width:280px;text-align:center}
.feature h3{font-family:"Raleway",sans-serif;font-weight:500;font-size:24px;color:var(--ink);margin:8px 0 12px}
.feature p{font-size:10.5px;line-height:19px;color:var(--muted)}
.feature svg{display:block;margin:0 auto}

.benefit-intro{left:144px;width:912px;top:1393px;text-align:center;font-size:15.5px;line-height:30px;color:var(--ink)}
.benefit{display:flex;align-items:center;gap:16px;font-family:"Raleway",sans-serif;font-size:22px;color:var(--blue)}

.subtitle{left:0;width:1200px;top:2012px;text-align:center;font-family:"Raleway",sans-serif;font-size:19px;color:var(--ink)}
.step-line{left:171px;width:2px;background:#d4d9e3}
.step-num{left:144px;width:54px;height:54px;border-radius:50%;display:flex;align-items:center;justify-content:center;font-family:"Raleway",sans-serif;font-size:22px;background:#eef1f7;color:#7b8090}
.step-num.current{background:var(--blue-strong);color:var(--white)}
.step{left:208px;width:360px}
.step h4{font-family:"Raleway",sans-serif;font-weight:500;font-size:22px;color:var(--ink)}
.step h4.current{color:var(--blue)}
.step p{font-size:10.5px;line-height:18px;color:var(--ink)}
.photo{left:648px;top:2080px;width:408px;height:347px}

.card{left:144px;width:408px;height:330px;background:var(--blue-strong);color:var(--white);padding:24px 22px}
.card h5{font-family:"Raleway",sans-serif;font-weight:400;font-size:24px}
.price{display:flex;align-items:flex-end;gap:14px;margin-top:4px;font-family:"Raleway",sans-serif}
.price small{font-size:16px;margin-bottom:10px}
.price strong{font-weight:800;font-size:62px;line-height:66px}
.price span{font-size:44px;font-weight:400;margin-left:-10px;line-height:60px}
.per{font-family:"Raleway",sans-serif;font-size:16px;margin-top:0}
.ticks{list-style:none;margin-top:14px}
.ticks li{font-size:10.5px;line-height:24px;display:flex;align-items:center;gap:10px}
.btn-dark{margin-top:14px;width:152px;height:38px;background:#101622;color:var(--white);font-family:"Raleway",sans-serif;font-weight:600;font-size:12px;display:flex;align-items:center;justify-content:center}

.side-title{left:647px;top:2656px;font-family:"Raleway",sans-serif;font-size:40px;color:var(--blue)}
.side-text{left:647px;top:2730px;width:420px;font-family:"Raleway",sans-serif;font-size:20px;line-height:34px;color:var(--ink)}

.quote{left:140px;width:920px;top:3646px;text-align:center;font-family:"Raleway",sans-serif;font-size:23px;line-height:37px;color:var(--ink)}
.author{left:0;width:1200px;top:3740px;text-align:center;font-family:"Raleway",sans-serif;font-size:15px;color:var(--blue)}
.dots{left:544px;top:3780px;display:flex;gap:16px}
.dots i{width:16px;height:16px;border-radius:50%;background:var(--dot);display:block}
.dots i.on{background:var(--blue-strong)}

.foot-links{left:144px;top:3991px;font-size:11px;color:var(--white);display:flex;gap:10px}
.copyright{left:144px;top:4027px;font-size:11px;color:var(--white)}
.social{left:898px;top:4008px;display:flex;gap:30px}
.social i{width:16px;height:16px;border-radius:50%;background:var(--white);display:block}
</style>
</head>
<body>

<svg class="backdrop" viewBox="0 0 1200 4082" aria-hidden="true">
  <polygon points="0,1263 1200,1186 1200,1799 0,1878" fill="#ebf0f9"/>
  <polygon points="0,2587 1200,2506 1200,3427 0,3505" fill="#ebf0f9"/>
  <polygon points="0,3955 1200,3876 1200,4082 0,4082" fill="#0f1a33"/>
</svg>

<!-- hero -->
<svg class="abs hero-photo" viewBox="0 0 1200 693" role="img" aria-label="Team working together at a desk with laptops, seen from above">
  <defs>
    <linearGradient id="heroShade" x1="0" y1="0" x2="1" y2="1">
      <stop offset="0" stop-color="#161d2a"/>
      <stop offset="0.6" stop-color="#283244"/>
      <stop offset="1" stop-color="#3a4352"/>
    </linearGradient>
  </defs>
  <polygon points="0,0 1200,0 1200,613 0,693" fill="url(#heroShade)"/>
</svg>

<div class="abs brand"><span class="brand-dot"></span>BRIGHTDUNE</div>
<nav class="abs nav">
  <span class="active">Home</span><span>That's how it's done</span><span>Prices</span><span>About us</span><span>Ask</span><span>Get started now</span>
</nav>

<h1 class="abs hero-title">Just work.</h1>
<p class="abs hero-text">In large companies, IT departments ensure a functioning IT. Central servers are used, which are accessed from the individual workstations.<br>BrightDune has set itself the goal of providing such a solution to small and medium-sized companies at manageable costs.</p>
<div class="abs btn-blue">GET STARTED LEARN</div>
<svg class="abs arrow" style="left:54px" width="20" height="28" viewBox="0 0 20 28"><path d="M15 3 L5 14 L15 25" stroke="#fff" stroke-width="4" fill="none"/></svg>
<svg class="abs arrow" style="left:1126px" width="20" height="28" viewBox="0 0 20 28"><path d="M5 3 L15 14 L5 25" stroke="#fff" stroke-width="4" fill="none"/></svg>

<!-- IT that just works -->
<h2 class="abs section-title" style="top:766px">IT that just works</h2>

<div class="abs feature" style="left:145px;top:842px">
  <svg width="60" height="60" viewBox="0 0 60 60"><circle cx="30" cy="30" r="27" stroke="#222" stroke-width="2" fill="none"/><circle cx="30" cy="17" r="3" stroke="#222" stroke-width="2" fill="none"/><rect x="26" y="25" width="8" height="22" rx="2" stroke="#222" stroke-width="2" fill="none"/></svg>
  <h3>The problem</h3>
  <p>The basis of the IT problems that unnecessarily compli-<br>cate your daily business is - in addition to the human<br>factor - the computer itself, because there are viruses<br>landing programs are paralyzed and lost data.</p>
</div>
<div class="abs feature" style="left:459px;top:842px">
  <svg width="60" height="60" viewBox="0 0 60 60"><path d="M8 46 L22 38 L38 42 L52 32" stroke="#222" stroke-width="2" fill="none"/><path d="M22 8 h10 v6 a4 4 0 1 1 0 6 v8 h-8 a4 4 0 1 0 -6 0 h-6 v-10 a4 4 0 1 1 0 -6 z" stroke="#222" stroke-width="2" fill="none"/></svg>
  <h3>Our Solution</h3>
  <p>BrightDune provides you with a solution that ensures<br>the daily backup of your data and the monitoring of the<br>operational readiness of your system. That's what we do<br>at the base: everything you need to work on is moved to<br>the servers in our data center. All necessary legal and<br>other requirements are implemented by us.</p>
</div>
<div class="abs feature" style="left:776px;top:842px">
  <svg width="60" height="60" viewBox="0 0 60 60"><path d="M30 4 L52 12 V30 C52 44 42 52 30 57 C18 52 8 44 8 30 V12 Z" stroke="#222" stroke-width="2" fill="none"/><circle cx="30" cy="30" r="10" stroke="#222" stroke-width="2" fill="none"/><path d="M25 30 L29 34 L35 26" stroke="#222" stroke-width="2" fill="none"/></svg>
  <h3>Your Safety</h3>
  <p>If you're wondering how secure our solution is, the<br>answer is simple: very safe. We work with Northgate, one of<br>Germany's largest data centers. The security features of<br>this data center are similar to those of a high-security<br>system. Their data is protected against malicious soft-<br>ware, unauthorized access and even natural disasters,<br>and in the event of a power failure, generators and<br>backup batteries ensure continuous operation.</p>
</div>

<!-- Benefits -->
<h2 class="abs section-title" style="top:1336px">Benefits</h2>
<p class="abs benefit-intro">Explode resources for your core business, because you do not have to worry about time-consuming malfunctions such as lame programs, virus attacks, data loss, etc., nor do you have to book an external service provider for rectification. Capacity and storage issues are a thing of the past, and your operating system is updated by the data center - faster, more direct, and much safer than what you could do on-site. If you use our ThinClients, further investments in your EDP infrastructure will be avoided.</p>

<div class="abs benefit" style="left:144px;top:1572px"><svg width="28" height="24" viewBox="0 0 28 24"><rect x="1" y="6" width="18" height="12" rx="2" fill="#1a5aa8"/><path d="M19 9 h5 l3 4 v5 h-8z" fill="#1a5aa8"/><circle cx="7" cy="20" r="3" fill="#1a5aa8"/><circle cx="22" cy="20" r="3" fill="#1a5aa8"/></svg>Express suppression</div>
<div class="abs benefit" style="left:144px;top:1627px"><svg width="28" height="24" viewBox="0 0 28 24"><path d="M24 2 C14 2 8 10 6 16 L10 20 C16 18 24 12 24 2Z" fill="#1a5aa8"/><path d="M6 16 L2 22 L8 20Z" fill="#1a5aa8"/></svg>Fast programs</div>
<div class="abs benefit" style="left:144px;top:1683px"><svg width="28" height="24" viewBox="0 0 28 24"><path d="M8 11 V7 a6 6 0 0 1 12 0 V11" stroke="#1a5aa8" stroke-width="3" fill="none"/><rect x="5" y="11" width="18" height="12" rx="2" fill="#1a5aa8"/></svg>Professional protection</div>

<div class="abs benefit" style="left:528px;top:1572px"><svg width="28" height="24" viewBox="0 0 28 24"><path d="M5 10 A9 9 0 0 1 22 8" stroke="#1a5aa8" stroke-width="3" fill="none"/><path d="M23 14 A9 9 0 0 1 6 16" stroke="#1a5aa8" stroke-width="3" fill="none"/><path d="M18 8 h6 v-6z" fill="#1a5aa8"/><path d="M10 16 h-6 v6z" fill="#1a5aa8"/></svg>Data backup</div>
<div class="abs benefit" style="left:528px;top:1627px"><svg width="28" height="24" viewBox="0 0 28 24"><rect x="2" y="3" width="24" height="5" fill="#1a5aa8"/><rect x="2" y="10" width="24" height="5" fill="#1a5aa8"/><rect x="2" y="17" width="24" height="5" fill="#1a5aa8"/></svg>sustained</div>
<div class="abs benefit" style="left:528px;top:1683px"><svg width="28" height="24" viewBox="0 0 28 24"><rect x="1" y="6" width="26" height="13" fill="#1a5aa8"/><circle cx="14" cy="12.5" r="3.5" fill="#ebf0f9"/></svg>Predictable costs</div>

<div class="abs benefit" style="left:853px;top:1572px"><svg width="28" height="24" viewBox="0 0 28 24"><path d="M7 20 a6 6 0 0 1 0-12 a8 8 0 0 1 15 2 a5 5 0 0 1 0 10z" fill="#1a5aa8"/><path d="M14 17 v-7 M10 13 l4-4 l4 4" stroke="#ebf0f9" stroke-width="2" fill="none"/></svg>Updates</div>
<div class="abs benefit" style="left:853px;top:1627px"><svg width="28" height="24" viewBox="0 0 28 24"><path d="M14 2 L24 6 V12 C24 18 19 21 14 23 C9 21 4 18 4 12 V6Z" fill="#1a5aa8"/><path d="M14 5 V20 C10 18 7 16 7 12 V8Z" fill="#ebf0f9"/></svg>High security</div>
<div class="abs benefit" style="left:853px;top:1683px"><svg width="28" height="24" viewBox="0 0 28 24"><circle cx="14" cy="12" r="8" fill="none" stroke="#1a5aa8" stroke-width="5" stroke-dasharray="3 2.2"/><circle cx="14" cy="12" r="6" fill="#1a5aa8"/><circle cx="14" cy="12" r="2.5" fill="#ebf0f9"/></svg>Used software</div>

<!-- How do I become a customer -->
<h2 class="abs section-title" style="top:1956px">How do I become a customer?</h2>
<p class="abs subtitle">To become a BrightDune customer requires the following four steps.</p>

<div class="abs step-line" style="top:2133px;height:264px"></div>
<div class="abs step-num current" style="top:2079px">1</div>
<div class="abs step-num" style="top:2178px">2</div>
<div class="abs step-num" style="top:2282px">3</div>
<div class="abs step-num" style="top:2370px">4</div>

<div class="abs step" style="top:2074px"><h4 class="current">Select service</h4><p>BrightDune offers two different models. Choose one of these<br>models.</p></div>
<div class="abs step" style="top:2171px"><h4>Send an inquiry</h4><p>Fill out our form for a contract request without obligation. We<br>evaluate the feasibility and draft a contract.</p></div>
<div class="abs step" style="top:2275px"><h4>Sign a contract</h4><p>The signed contract can be sent to us by post or by e-mail.</p></div>
<div class="abs step" style="top:2363px"><h4>Work loose</h4><p>Once the contract has been entered, you can start work within five<br>working days.</p></div>

<svg class="abs photo" viewBox="0 0 408 347" role="img" aria-label="Smiling businessman shaking hands in a warm office">
  <defs>
    <linearGradient id="photoShade" x1="0" y1="0" x2="1" y2="1">
      <stop offset="0" stop-color="#6b4b33"/>
      <stop offset="0.5" stop-color="#7d8fae"/>
      <stop offset="1" stop-color="#2c3a57"/>
    </linearGradient>
  </defs>
  <rect width="408" height="347" fill="url(#photoShade)"/>
</svg>

<!-- Pricing -->
<div class="abs card" style="top:2669px">
  <h5>Thin client</h5>
  <div class="price"><small>from</small><strong>99</strong><span>€</span></div>
  <p class="per">per user / month (from 5 users)</p>
  <ul class="ticks">
    <li><svg width="10" height="8" viewBox="0 0 10 8"><path d="M1 4 L4 7 L9 1" stroke="#fff" stroke-width="2" fill="none"/></svg>Up to 5 users 115 € / month</li>
    <li><svg width="10" height="8" viewBox="0 0 10 8"><path d="M1 4 L4 7 L9 1" stroke="#fff" stroke-width="2" fill="none"/></svg>Minimum term 12 months</li>
    <li><svg width="10" height="8" viewBox="0 0 10 8"><path d="M1 4 L4 7 L9 1" stroke="#fff" stroke-width="2" fill="none"/></svg>Thinclient per user included</li>
    <li><svg width="10" height="8" viewBox="0 0 10 8"><path d="M1 4 L4 7 L9 1" stroke="#fff" stroke-width="2" fill="none"/></svg>Max. 8 hours reaction time</li>
  </ul>
  <div class="btn-dark">GET STARTED NOW</div>
</div>
<div class="abs card" style="top:3010px">
  <h5>Bring Your OWN</h5>
  <div class="price"><small>from</small><strong>75</strong><span>€</span></div>
  <p class="per">per user / month (from 5 users)</p>
  <ul class="ticks">
    <li><svg width="10" height="8" viewBox="0 0 10 8"><path d="M1 4 L4 7 L9 1" stroke="#fff" stroke-width="2" fill="none"/></svg>Up to 5 users 85 € / month</li>
    <li><svg width="10" height="8" viewBox="0 0 10 8"><path d="M1 4 L4 7 L9 1" stroke="#fff" stroke-width="2" fill="none"/></svg>No minimum term</li>
    <li><svg width="10" height="8" viewBox="0 0 10 8"><path d="M1 4 L4 7 L9 1" stroke="#fff" stroke-width="2" fill="none"/></svg>Use with own terminal</li>
    <li><svg width="10" height="8" viewBox="0 0 10 8"><path d="M1 4 L4 7 L9 1" stroke="#fff" stroke-width="2" fill="none"/></svg>Max. 8 hours reaction time</li>
  </ul>
  <div class="btn-dark">GET STARTED NOW</div>
</div>

<h2 class="abs side-title">Select service</h2>
<p class="abs side-text">Choose your service. BrightDune provides a complete workstation in the Thin Client model. All you need is a monitor to get started.<br><br>Both services can be encrypted using an existing PC, laptop or tablet from any location.</p>

<!-- Testimonials -->
<h2 class="abs section-title" style="top:3578px">What our customers say</h2>
<p class="abs quote">"I recently started my business. The monthly payment of the services offers high financial flexibility. "</p>
<p class="abs author">Mark Feldner,&nbsp; Quality Consultant</p>
<div class="abs dots"><i class="on"></i><i></i><i></i><i></i></div>

<!-- Footer -->
<div class="abs foot-links"><span>Home</span><span>|</span><span>That's how it's done</span><span>|</span><span>Prices</span><span>|</span><span>About Us</span><span>|</span><span>Ask</span><span>|</span><span>Get Started now</span></div>
<p class="abs copyright">Copyright © 2019 &nbsp;Bright Dune. &nbsp;All rights reserved.</p>
<div class="abs social" aria-label="Social media links"><i></i><i></i><i></i><i></i></div>

</body>
</html>
```